Anzeige zur Kundenakquise
Zielgruppe
Wir sind der größte unabhängige Versicherungsmakler Deutschlands.
https://www.vendler-tarifkreis.de/
Aufgabenstellung
Die Anzeige dient zur Kundenakquise. Der Flyer soll in erster Linie auf Trivolo veröffentlicht werden.
Sie soll Kunden anregen eine Nachricht an uns zu schicken und einen Termin bis zum 30.11.2018 zu vereinbaren um ihre KFZ-Versicherungen vergleichen zu lassen.
Der alte Flyer wird mit hochgeladen. Bitte den Text nicht 1 zu 1 übernehmen.
Farbe und Stil sollten übernommen werden.
Die Maße für Trivolo:
Empfohlene Bildgröße:
1.200 x 628 Pixel
Bildseitenverhältnis: 1,91:1
Auf Grund der Zusendung von mehrerern Flyer der Designer bitte ich die Anzahl auf 3 zu einigen, d.h. bitte senden Sie für eine Trivolo Slidekampane 3 Flyer als ein Projekt zu. Vielen Dank für Ihre Mühe.

```html
<!DOCTYPE html>
<html lang="de">
<head>
<meta charset="utf-8">
<title>Anzeige KFZ-Versicherung wechseln</title>
<link href="https://fonts.googleapis.com/css2?family=Barlow:wght@300;400;700;800&display=swap" rel="stylesheet">
<style>
  :root {
    --stage: #e4e4e4;
    --paper: #ffffff;
    --band-grey: #7b7a7a;
    --brand-green: #8fb52c;
    --text-dark: #1e1e1e;
    --logo-grey: #4a4a4a;
    --photo-light: #f1efee;
    --photo-warm: #dcc5b8;
  }
  html, body {
    margin: 0;
    width: 1200px;
    height: 1200px;
    overflow: hidden;
    background: var(--stage);
  }
  .ad {
    position: absolute;
    left: 0;
    top: 286px;
    width: 1200px;
    height: 628px;
    background: var(--paper);
    overflow: hidden;
    font-family: "Barlow", "Helvetica Neue", Arial, sans-serif;
  }
  .top-band {
    position: absolute;
    left: 0; top: 0;
    width: 100%; height: 100px;
    background: var(--band-grey);
  }
  .photo {
    position: absolute;
    left: 0; top: 100px;
    width: 650px; height: 528px;
    background: linear-gradient(180deg, var(--photo-warm) 0%, var(--photo-light) 100%);
  }
  .deadline {
    position: absolute;
    left: 0; top: 30px;
    width: 585px; height: 86px;
    background: var(--brand-green);
    color: #fff;
    font-weight: 300;
    font-size: 50px;
    letter-spacing: 1px;
    line-height: 86px;
    padding-left: 40px;
    box-sizing: border-box;
  }
  .headline {
    position: absolute;
    left: 230px; top: 116px;
    width: 970px; height: 84px;
    margin: 0;
    background: var(--brand-green);
    color: #fff;
    font-weight: 800;
    font-size: 46px;
    letter-spacing: 1.5px;
    line-height: 84px;
    padding-left: 36px;
    box-sizing: border-box;
    white-space: nowrap;
  }
  .offer {
    position: absolute;
    left: 690px; top: 262px;
    width: 460px;
    color: var(--text-dark);
    font-size: 21px;
    line-height: 1.4;
    letter-spacing: 0.3px;
  }
  .offer p { margin: 0 0 18px; }
  .offer strong { font-weight: 700; }
  .brand {
    position: absolute;
    right: 50px; top: 520px;
    display: flex;
    align-items: center;
    gap: 12px;
  }
  .brand-square {
    width: 52px; height: 52px;
    background: var(--brand-green);
  }
  .brand-name {
    color: var(--logo-grey);
    font-weight: 700;
    font-size: 24px;
    line-height: 1.05;
    letter-spacing: 0.5px;
    text-transform: uppercase;
  }
</style>
</head>
<body>
  <section class="ad">
    <div class="top-band"></div>
    <div class="photo" role="img" aria-label="Foto: schützende Hände über einem roten Auto"></div>
    <div class="deadline">STICHTAG 30.11.2018</div>
    <h1 class="headline">JETZT KFZ-VERSICHERUNG WECHSELN</h1>
    <div class="offer">
      <p>Wir prüfen für Sie mehr als 70 Versicherer und finden den passenden Tarif für Ihr Fahrzeug. <strong>Natürlich kostenlos!</strong></p>
      <p>Schreiben Sie uns und sichern Sie sich Ihren Termin!</p>
    </div>
    <div class="brand">
      <div class="brand-square"></div>
      <div class="brand-name">Vendler<br>Tarifkreis</div>
    </div>
  </section>
</body>
</html>
```